Corporate Brightfen business cards to be handed to investor, bankers etc. Needs to have a young feel

I need business cards designed for a technology company that provides uber-like rapid response on the security industry. I would like it simple but very cool and tasteful. See attached documents for artwork and colours to be used. Cut sheet describes business model. Card stock should be thicker than normal. I would like the one side to be just the art and the other to have the contact info with maybe the pin somewhere.

Target Market(s)

Investors

Industry/Entity Type

Business

Contact Information for Business Card

Would like the logo attached on one side with name address and other info on the other side.

Font styles to use
Other font styles liked:
• See existing logo

Colors
6b449b
886aae
e4daeb
ffffff

Requirements
Must have
• Name: Dorian Felkatsis
• Address: 47 Larkfield Avenue, Toronto, On, M6K2B7
• Tel: 416-7291846
• Email: rolo@brightfen.io
Nice to have
• See logo colours

```html
<!DOCTYPE html>
<html lang="en">
<head>
<meta charset="utf-8">
<title>Brightfen Business Card</title>
<link href="https://fonts.googleapis.com/css2?family=Nunito:wght@400;700&display=swap" rel="stylesheet">
<style>
  :root {
    --purple-deep: #6b449b;
    --purple-mid: #886aae;
    --lavender: #e4daeb;
    --white: #ffffff;
    --ink: #1c1a1d;
    --page: #ffffff;
  }
  * { margin: 0; padding: 0; box-sizing: border-box; }
  html, body {
    width: 1200px; height: 1200px; overflow: hidden;
    background: var(--page);
    font-family: "Nunito", sans-serif;
  }
  .canvas { position: relative; width: 1200px; height: 1200px; }
  .card {
    position: absolute; left: 168px; width: 858px; height: 491px;
    background: var(--white);
    box-shadow: 5px 6px 7px rgba(0,0,0,0.28);
    overflow: hidden;
  }
  .card--front { top: 63px; }
  .card--back { top: 632px; }

  .brand {
    position: absolute; left: 0; right: 0; top: 240px;
    display: flex; justify-content: center; align-items: center; gap: 12px;
  }
  .brand__dot {
    width: 32px; height: 32px; border-radius: 50%;
    background: var(--purple-mid);
  }
  .brand__name {
    font-size: 64px; font-weight: 400; color: var(--ink);
    letter-spacing: -1px; line-height: 1;
  }

  .holder-name {
    position: absolute; left: 0; right: 0; top: 112px;
    text-align: center;
    font-size: 35px; font-weight: 700; color: var(--purple-deep);
    letter-spacing: 0.3px;
  }
  .contact-row {
    position: absolute; left: 0; width: 100%; height: 76px;
    background: var(--lavender);
  }
  .contact-row--address { top: 250px; }
  .contact-row--phone { top: 333px; }
  .contact-row--email { top: 416px; height: 76px; }
  .contact-row__icon {
    position: absolute; left: 0; top: 0; width: 76px; height: 100%;
    background: var(--purple-mid);
    display: flex; align-items: center; justify-content: center;
  }
  .contact-row__icon svg { width: 40px; height: 40px; fill: var(--lavender); }
  .contact-row__text {
    position: absolute; left: 0; right: 0; top: 0; height: 100%;
    display: flex; align-items: center; justify-content: center;
    font-size: 17px; color: var(--purple-deep); letter-spacing: 0.3px;
  }
</style>
</head>
<body>
<div class="canvas">
  <section class="card card--front">
    <div class="brand">
      <span class="brand__dot"></span>
      <span class="brand__name">brightfen</span>
    </div>
  </section>

  <section class="card card--back">
    <h1 class="holder-name">DORIAN FELKATSIS</h1>

    <div class="contact-row contact-row--address">
      <div class="contact-row__icon">
        <svg viewBox="0 0 40 40" aria-hidden="true"><path d="M20 5 L37 20 L33 20 L33 35 L24 35 L24 25 L16 25 L16 35 L7 35 L7 20 L3 20 Z M28 7 L32 7 L32 13 L28 10 Z"/></svg>
      </div>
      <div class="contact-row__text">47 Larkfield Avenue, Toronto, On, M6K2B7</div>
    </div>

    <div class="contact-row contact-row--phone">
      <div class="contact-row__icon">
        <svg viewBox="0 0 40 40" aria-hidden="true"><path d="M13 4 C15 3 16 4 17 6 L19 12 C19.5 14 19 15 17 16 L15 17 C15 22 18 28 22 31 L24 30 C26 29 27 29 28 31 L31 36 C32 38 31 39 29 39.5 C18 41 7 22 9 9 C9.5 6 11 5 13 4 Z"/></svg>
      </div>
      <div class="contact-row__text">416-7291846</div>
    </div>

    <div class="contact-row contact-row--email">
      <div class="contact-row__icon">
        <svg viewBox="0 0 40 40" aria-hidden="true"><path fill-rule="evenodd" d="M20 2 C30.5 2 38 9 38 18 C38 25 34 29 29 29 C26.5 29 25 27.5 24.7 26 C23 28 21 29 18.5 29 C14 29 11 25.5 11 21 C11 15 15.5 10 21 10 C23.5 10 25 11 26 12.5 L26.5 11 L31 11 L29 23 C28.8 24.5 29.3 25 30 25 C32 25 34 22.5 34 18 C34 11 28 6 20 6 C11.5 6 6 12.5 6 20.5 C6 29 12 34 20 34 C23.5 34 26 33.3 28.5 32 L30 35.5 C27 37 24 38 20 38 C10 38 2 31.5 2 20.5 C2 10 10 2 20 2 Z M21.5 14 C18 14 15.8 17 15.8 20.5 C15.8 23.2 17.3 25 19.6 25 C23 25 25 21.8 25 18.5 C25 15.8 23.6 14 21.5 14 Z"/></svg>
      </div>
      <div class="contact-row__text">rolo@brightfen.io</div>
    </div>
  </section>
</div>
</body>
</html>
```